Web Design Project for Web Agency

WHAT I NEED:
The design I need (PSD file) is for a microsite designed for employee recruitment for Brennick, a Web agency.
***Design for the 1st Page ONLY : "Manifeste"
OBJECTIVES OF THE WEBSITE:
1. To promote the agency's corporate culture and HR management principles.
2. To get people to apply on available jobs
ELEMENTS OF THE PAGE "MANIFESTE" :
1. Brennick logo (see attached files). Beside the logo must be the word "Carrières" ("Careers" in english)
***The logo is not final and there is NO branding for Brennick yet. That is why there are multiple files. So please feel free to be creative!
2. Main menu : 4 sections
Manifeste | Opportunités | Brenick | Postuler
3. Manifeste :
This page is the home page. It will present 2 main sections :
a. The agency's corporate culture :
- Title of the page is a question : "Do you embrace Brennick's corporate culture?"
- Then, presentation of the 5 corporate values, each with a title and short description
- At the end of the list of values, we want a button that says "Apply now"
b. The agency's HR management principles :
- Title of the page is a question : "Do you see yourself working at Brennick?"
- Then, presentation of the 5 Management principles, each with a title and short description
- At the end of the list of principles, we want a button that says "Apply now"
VISUAL INSPIRATION
To create each section of the "Manifeste" page, we want a design that will fit with the corporate culture:
- Brennick is BOLD
- Brennick is PROUD
- Brennick is PROFESSIONAL
- Brennick is ELEGANT
- Brennick is REFINED
We want something slick and modern. Here are some Website's that we like that can be of inspiration:
- http://www.studio-varnel.com/en/services
- http://quillmorrowlab.com/

```html
<!DOCTYPE html>
<html lang="en">
<head>
<meta charset="utf-8">
<title>Brennick Careers – Manifeste</title>
<link href="https://fonts.googleapis.com/css2?family=Open+Sans:wght@400;600;700;800&family=Great+Vibes&display=swap" rel="stylesheet">
<style>
:root{
  --blue:#1e9ad6;
  --blue-light:#cfe9f7;
  --orange:#f26b21;
  --green:#5aab2e;
  --ink:#333;
  --muted:#777;
  --grey-bg:#f1f1f1;
  --line:#d9d9d9;
  --dark:#2f2f2f;
  --darker:#232323;
  --white:#fff;
}
*{box-sizing:border-box;margin:0;padding:0}
html,body{width:1200px;height:2624px;overflow:hidden}
body{font-family:"Open Sans",Arial,sans-serif;color:var(--ink);background:var(--white)}
section,header,footer{position:relative;width:1200px}

/* header */
.site-header{height:88px;display:flex;align-items:center;justify-content:space-between;padding:0 40px;border-bottom:1px solid var(--line)}
.brand-name{font-size:40px;font-weight:800;color:var(--ink);line-height:1}
.brand-tag{font-size:11px;letter-spacing:3px;color:var(--muted);margin-top:4px}
.main-nav{display:flex;height:88px;margin-right:60px}
.main-nav a{width:120px;display:flex;flex-direction:column;align-items:center;justify-content:center;gap:8px;font-size:17px;color:var(--muted);text-decoration:none}
.main-nav a.active{background:var(--blue-light);color:var(--blue)}
.main-nav svg{width:22px;height:22px}

/* hero */
.hero{height:440px;background:linear-gradient(90deg,#e9ecef 0%,#dfe3e7 45%,#c9d3dc 100%);overflow:hidden}
.hero-photo{position:absolute;right:110px;top:0;width:420px;height:440px;background:linear-gradient(180deg,#e6d6b7 0%,#f1e6d6 40%,#e3e6ea 100%)}
.hero-text{position:absolute;left:90px;top:70px;width:560px;text-align:center}
.hero-hello{font-family:"Great Vibes",cursive;font-size:46px;color:var(--ink);margin-left:150px;text-align:left;line-height:1.2}
.hero-title{font-size:36px;font-weight:600;letter-spacing:2px;line-height:1.3;margin-top:2px;white-space:nowrap}
.hero-title strong{font-weight:800;display:block;font-size:36px}
.btn{display:inline-flex;align-items:center;gap:10px;background:var(--orange);color:var(--white);font-weight:600;font-size:18px;padding:12px 26px;border-radius:24px;text-decoration:none}
.hero .btn{margin-top:32px}
.hero-arrow{position:absolute;top:208px;width:24px;height:24px}
.hero-arrow.left{left:18px}.hero-arrow.right{right:18px}
.spacer{height:10px}

/* why band */
.why-band{height:60px;background:var(--blue);color:var(--white);text-align:center;font-size:30px;font-weight:600;line-height:60px;z-index:1}
.why-band::after{content:"";position:absolute;left:50%;bottom:-12px;margin-left:-12px;border:12px solid transparent;border-bottom:0;border-top-color:var(--blue)}
.features{height:240px;display:flex;justify-content:center;gap:120px;padding-top:30px}
.feature{width:260px;text-align:center}
.feature svg{width:44px;height:44px}
.feature h3{font-size:18px;font-weight:600;margin:6px 0 6px}
.feature p{font-size:13px;color:var(--muted);line-height:1.45}
.feature .more{font-size:13px;font-weight:700;color:var(--ink);margin-top:8px}
.t-orange{color:var(--orange)}.t-blue{color:var(--blue)}.t-green{color:var(--green)}

/* values */
.values{background:var(--grey-bg);border-top:1px solid var(--line)}
.values.culture{height:562px}
.values.working{height:490px}
.section-title{text-align:center;font-size:38px;font-weight:400;color:var(--blue);display:flex;align-items:center;justify-content:center;gap:24px}
.section-title::before,.section-title::after{content:"";width:90px;height:1px;background:var(--blue)}
.culture .section-title{padding-top:28px}
.working .section-title{padding-top:24px}
.value-grid{position:relative;width:1040px;margin:36px auto 0;height:330px}
.working .value-grid{height:300px;margin-top:30px}
.value{position:absolute;width:300px}
.value h4{display:flex;align-items:center;gap:14px;font-size:22px;font-weight:400}
.value .num{width:34px;height:28px;background:var(--dark);color:var(--white);font-size:14px;font-weight:700;display:flex;align-items:center;justify-content:center}
.value p{font-size:14px;color:var(--muted);line-height:1.5;margin-top:14px}
.value.hl h4{color:var(--orange)}
.divider-h{position:absolute;left:0;right:0;top:150px;border-top:1px dashed var(--line)}
.divider-v{position:absolute;border-left:1px dashed var(--line)}
.apply{text-align:center}
.apply .btn{border-radius:3px;padding:10px 24px;font-size:17px}

/* communicate */
.communicate{height:290px;text-align:center;padding-top:40px;border-top:1px solid var(--line)}
.communicate h2{font-size:36px;font-weight:400}
.communicate p{font-size:19px;color:var(--ink);line-height:1.45;margin-top:24px}
.communicate p span{color:var(--blue)}
.subscribe{display:flex;justify-content:center;margin-top:26px}
.subscribe .field{width:380px;height:40px;border:1px solid var(--line);font-size:13px;color:#aaa;text-align:left;padding:11px 14px}
.subscribe .go{height:40px;background:var(--blue);color:var(--white);font-size:16px;font-weight:600;padding:9px 28px;margin-left:6px}

/* social */
.social{height:190px;text-align:center;padding-top:44px;border-top:1px solid var(--line)}
.social h2{font-size:38px;font-weight:400}
.social-list{display:flex;justify-content:center;gap:14px;margin-top:28px}
.social-list span{width:40px;height:40px;border-radius:50%;background:#666}

/* footer */
.site-footer{height:170px;background:var(--dark);color:#bbb;display:flex;justify-content:space-between;padding:30px 140px 0}
.site-footer::before{content:"";position:absolute;left:50%;top:-1px;margin-left:-12px;border:12px solid transparent;border-bottom:0;border-top-color:var(--white)}
.site-footer h5{font-size:16px;font-weight:600;color:var(--white);margin-bottom:12px}
.post{display:flex;gap:18px}
.post-photo{width:150px;height:80px;background:linear-gradient(135deg,#dedede,#9a9a9a)}
.post p{font-size:14px;color:var(--white);width:260px}
.post small{display:block;font-size:12px;color:#aaa;margin-top:6px;line-height:1.4}
.contact{width:270px;font-size:12px;line-height:1.5}
.contact div{display:flex;align-items:center;gap:8px;margin-top:6px}
.contact svg{width:14px;height:14px}
.bottom-bar{height:84px;display:flex;justify-content:space-between;align-items:center;padding:0 140px;font-size:14px;color:var(--muted)}
.bottom-bar nav{display:flex;gap:22px;color:var(--ink)}
</style>
</head>
<body>

<header class="site-header">
  <div class="brand">
    <div class="brand-name">Brennick</div>
    <div class="brand-tag">AGENCE NUMÉRIQUE</div>
  </div>
  <nav class="main-nav">
    <a class="active" href="#"><svg viewBox="0 0 24 24" fill="none" stroke="currentColor" stroke-width="2"><rect x="4" y="3" width="16" height="18"/><path d="M8 8h8M8 12h8M8 16h5"/></svg>Manifeste</a>
    <a href="#"><svg viewBox="0 0 24 24" fill="none" stroke="currentColor" stroke-width="2"><rect x="3" y="7" width="18" height="13"/><path d="M9 7V4h6v3"/></svg>Opportunités</a>
    <a href="#"><svg viewBox="0 0 24 24" fill="none" stroke="currentColor" stroke-width="2"><path d="M3 21V10l9-6 9 6v11z"/></svg>Brennick</a>
    <a href="#"><svg viewBox="0 0 24 24" fill="none" stroke="currentColor" stroke-width="2"><path d="M4 20l4-1 11-11-3-3L5 16z"/></svg>Postuler</a>
  </nav>
</header>

<section class="hero">
  <div class="hero-photo" role="img" aria-label="Photo of a smiling recruiter in a bright office"></div>
  <div class="hero-text">
    <div class="hero-hello">Hello</div>
    <h1 class="hero-title">WELCOME, WE ARE<strong>BRENNICK WEB AGENCY</strong></h1>
    <a class="btn" href="#">View Recruitment
      <svg width="16" height="12" viewBox="0 0 16 12"><path d="M0 6h13M9 1l5 5-5 5" stroke="#fff" stroke-width="2" fill="none"/></svg></a>
  </div>
  <svg class="hero-arrow left" viewBox="0 0 24 24"><path d="M16 4L8 12l8 8" fill="#555"/></svg>
  <svg class="hero-arrow right" viewBox="0 0 24 24"><path d="M8 4l8 8-8 8" fill="#555"/></svg>
</section>
<div class="spacer"></div>

<section class="why-band">Why Choose Us?</section>
<section class="features">
  <div class="feature">
    <svg viewBox="0 0 44 44" fill="none" stroke="#f26b21" stroke-width="2.5"><rect x="9" y="6" width="26" height="32"/><path d="M15 14h14M15 21h14M15 28h9"/></svg>
    <h3 class="t-orange">MANIFESTO</h3>
    <p>Improve your packaging workflow by ensuring that right the information is collected avoiding additional</p>
    <div class="more">Read More...</div>
  </div>
  <div class="feature">
    <svg viewBox="0 0 44 44" fill="none" stroke="#1e9ad6" stroke-width="2.5"><circle cx="22" cy="22" r="8"/><path d="M22 4v6M22 34v6M4 22h6M34 22h6M9 9l4 4M31 31l4 4M35 9l-4 4M13 31l-4 4"/></svg>
    <h3 class="t-blue">CORPORATE CULTURE</h3>
    <p>Improve your packaging workflow by ensuring that right the information is collected avoiding additional</p>
    <div class="more">Read More...</div>
  </div>
  <div class="feature">
    <svg viewBox="0 0 44 44" fill="none" stroke="#5aab2e" stroke-width="2.5"><rect x="5" y="7" width="34" height="24"/><path d="M16 38h12M22 31v7"/><path d="M15 19l5 5 9-9"/></svg>
    <h3 class="t-green">HR MANAGEMENT</h3>
    <p>Improve your packaging workflow by ensuring that right the information is collected avoiding additional</p>
    <div class="more">Read More...</div>
  </div>
</section>

<section class="values culture">
  <h2 class="section-title">Do you embrace Brennick's corporate culture?</h2>
  <div class="value-grid">
    <div class="divider-h"></div>
    <div class="divider-v" style="left:345px;top:0;height:130px"></div>
    <div class="divider-v" style="left:690px;top:0;height:130px"></div>
    <div class="divider-v" style="left:520px;top:170px;height:130px"></div>
    <div class="value" style="left:0;top:0"><h4><span class="num">01</span>Corporate values</h4><p>Lorem Ipsum is simply dummy text of printing and typesetting industry. Lorem Ipsum has been industry.</p></div>
    <div class="value hl" style="left:370px;top:0"><h4><span class="num">02</span>Corporate values</h4><p>Lorem Ipsum is simply dummy text of printing and typesetting industry. Lorem Ipsum has been industry.</p></div>
    <div class="value" style="left:720px;top:0"><h4><span class="num">03</span>Corporate values</h4><p>Lorem Ipsum is simply dummy text of printing and typesetting industry. Lorem Ipsum has been industry.</p></div>
    <div class="value" style="left:190px;top:175px"><h4><span class="num">04</span>Corporate values</h4><p>Lorem Ipsum is simply dummy text of printing and typesetting industry. Lorem Ipsum has been industry.</p></div>
    <div class="value" style="left:550px;top:175px"><h4><span class="num">05</span>Corporate values</h4><p>Lorem Ipsum is simply dummy text of printing and typesetting industry. Lorem Ipsum has been industry.</p></div>
  </div>
  <div class="apply"><a class="btn" href="#">Apply Now
    <svg width="16" height="12" viewBox="0 0 16 12"><path d="M0 6h13M9 1l5 5-5 5" stroke="#fff" stroke-width="2" fill="none"/></svg></a></div>
</section>

<section class="communicate">
  <h2>Feel Free to Communicate</h2>
  <p><span>Contact Us</span> and let us know if you have any questions<br>Don't forget to View HR management principles and <span>subscribe to the news</span> below</p>
  <div class="subscribe"><div class="field">Enter email address</div><div class="go">Subscribe</div></div>
</section>

<section class="values working">
  <h2 class="section-title">Do you see yourself working at Brennick?</h2>
  <div class="value-grid">
    <div class="divider-h" style="top:140px"></div>
    <div class="divider-v" style="left:345px;top:0;height:120px"></div>
    <div class="divider-v" style="left:690px;top:0;height:120px"></div>
    <div class="divider-v" style="left:520px;top:160px;height:120px"></div>
    <div class="value" style="left:0;top:0"><h4><span class="num">01</span>Corporate values</h4><p>Lorem Ipsum is simply dummy text of printing and typesetting industry. Lorem Ipsum has been industry.</p></div>
    <div class="value" style="left:370px;top:0"><h4><span class="num">02</span>Corporate values</h4><p>Lorem Ipsum is simply dummy text of printing and typesetting industry. Lorem Ipsum has been industry.</p></div>
    <div class="value" style="left:720px;top:0"><h4><span class="num">03</span>Corporate values</h4><p>Lorem Ipsum is simply dummy text of printing and typesetting industry. Lorem Ipsum has been industry.</p></div>
    <div class="value" style="left:190px;top:165px"><h4><span class="num">04</span>Corporate values</h4><p>Lorem Ipsum is simply dummy text of printing and typesetting industry. Lorem Ipsum has been industry.</p></div>
    <div class="value" style="left:550px;top:165px"><h4><span class="num">05</span>Corporate values</h4><p>Lorem Ipsum is simply dummy text of printing and typesetting industry. Lorem Ipsum has been industry.</p></div>
  </div>
  <div class="apply"><a class="btn" href="#">Apply Now
    <svg width="16" height="12" viewBox="0 0 16 12"><path d="M0 6h13M9 1l5 5-5 5" stroke="#fff" stroke-width="2" fill="none"/></svg></a></div>
</section>

<section class="social">
  <h2>Socialise With Marlowe</h2>
  <div class="social-list"><span></span><span></span><span></span><span></span><span></span></div>
</section>

<footer class="site-footer">
  <div class="latest">
    <h5>Latest Post</h5>
    <div class="post">
      <div class="post-photo" role="img" aria-label="Blog post thumbnail photo"></div>
      <p>Lorem Ipsum is simply dummy text<small>Lorem Ipsum is simply dummy text of printing and typesetting industry text.</small></p>
    </div>
  </div>
  <div class="contact">
    <h5>Quick in Touch</h5>
    Send an email or just call us to get our services.
    <div><svg viewBox="0 0 14 14"><rect x="1" y="3" width="12" height="8" fill="none" stroke="#bbb"/><path d="M1 3l6 5 6-5" fill="none" stroke="#bbb"/></svg>info@brennickagency.com</div>
    <div><svg viewBox="0 0 14 14"><circle cx="7" cy="7" r="5.5" fill="none" stroke="#bbb"/><path d="M1.5 7h11M7 1.5v11" stroke="#bbb"/></svg>brennickagency.com</div>
  </div>
</footer>

<div class="bottom-bar">
  <nav><span>Manifeste</span><span>Opportunités</span><span>Brennick</span><span>Postuler</span></nav>
  <div>Copyright © 2015 Brennick. All Rights Reserved.</div>
</div>

</body>
</html>
```